Business card for Northland's Blue Wagon.

Good day i am looking for a business card design for my business.
The name of the business is Northland's Blue Wagon. It is a van rental business that provides a driver and helper to the customer. Customer have use to van for small moves, studio or 1 bedroom, Moving furniture like couch or kitchen cabinets.
We are available evenings, weekends and holidays.
the means to contact us is by phone at 628-947-2071; By emails at Oakridge@northlandsbluewagon.net; or by social media, Facebook and Instagram.
You can see attached pictures of the van and or logo.

```html
<!DOCTYPE html>
<html lang="en">
<head>
<meta charset="utf-8">
<title>Northland's Blue Wagon – Business Card</title>
<link href="https://fonts.googleapis.com/css2?family=Montserrat:wght@400;500;700&display=swap" rel="stylesheet">
<style>
  :root {
    --brand-red: #c21f2b;
    --ink: #1b1b1b;
    --card: #f4f4f4;
    --backdrop: #e2e4e3;
  }
  * { box-sizing: border-box; margin: 0; padding: 0; }
  html, body {
    width: 1200px; height: 1200px; overflow: hidden;
    background: var(--backdrop);
    font-family: "Montserrat", Arial, sans-serif;
    color: var(--ink);
  }
  .sheet {
    width: 1200px; height: 1200px;
    display: flex; flex-direction: column; align-items: center; justify-content: center;
    gap: 60px;
  }
  .card {
    position: relative;
    width: 760px; height: 435px;
    background: var(--card);
    border-radius: 4px;
  }
  /* Front */
  .brand-mark {
    position: absolute; top: 70px; right: 46px;
    display: flex; align-items: center; gap: 12px;
    color: var(--brand-red);
    font-weight: 700; font-size: 22px; line-height: 1.2;
    text-align: left;
  }
  .brand-mark .dot {
    width: 18px; height: 18px; border-radius: 50%;
    background: var(--brand-red); flex: none;
  }
  .holder { position: absolute; left: 47px; top: 212px; }
  .holder-name {
    color: var(--brand-red); font-weight: 700; font-size: 33px; letter-spacing: 0.2px;
  }
  .holder-role { font-size: 19px; font-weight: 400; margin-top: 4px; }
  .divider {
    position: absolute; left: 45px; right: 45px; top: 289px;
    height: 2px; background: var(--brand-red);
  }
  .contacts {
    position: absolute; left: 45px; top: 304px;
    list-style: none;
    font-size: 19px;
  }
  .contacts li { display: flex; align-items: center; gap: 10px; height: 29px; }
  .contacts svg { width: 17px; height: 17px; flex: none; }
  .address {
    position: absolute; right: 45px; top: 330px;
    text-align: right; font-size: 19px; line-height: 29px;
  }
  /* Back */
  .card-back { display: flex; flex-direction: column; align-items: center; justify-content: center; }
  .back-mark {
    display: flex; align-items: center; gap: 14px;
    color: var(--brand-red); font-weight: 700; font-size: 34px;
    margin-top: -20px;
  }
  .back-mark .dot { width: 24px; height: 24px; border-radius: 50%; background: var(--brand-red); }
  .back-url {
    position: absolute; bottom: 58px; left: 0; right: 0;
    text-align: center; color: var(--brand-red); font-size: 19px;
  }
</style>
</head>
<body>
<main class="sheet">
  <section class="card card-front">
    <div class="brand-mark"><span class="dot"></span><span>Northland's<br>Blue Wagon</span></div>

    <div class="holder">
      <h1 class="holder-name">Ada Oakridge</h1>
      <p class="holder-role">Founder &amp; Director</p>
    </div>
    <div class="divider"></div>

    <ul class="contacts">
      <li>
        <svg viewBox="0 0 24 24" aria-hidden="true"><path fill="#c21f2b" d="M6.6 10.8a15.1 15.1 0 0 0 6.6 6.6l2.2-2.2a1 1 0 0 1 1-.25 11.4 11.4 0 0 0 3.6.57 1 1 0 0 1 1 1V20a1 1 0 0 1-1 1A17 17 0 0 1 3 4a1 1 0 0 1 1-1h3.5a1 1 0 0 1 1 1c0 1.25.2 2.45.57 3.57a1 1 0 0 1-.25 1z"/></svg>
        <span>628-947-2071</span>
      </li>
      <li>
        <svg viewBox="0 0 24 24" aria-hidden="true"><rect x="2" y="5" width="20" height="14" rx="1.5" fill="#c21f2b"/><path d="M3 6.5l9 6.5 9-6.5" fill="none" stroke="#f4f4f4" stroke-width="1.8"/></svg>
        <span>Oakridge@northlandsbluewagon.net</span>
      </li>
      <li>
        <svg viewBox="0 0 24 24" aria-hidden="true"><circle cx="12" cy="12" r="10" fill="#c21f2b"/><path d="M2 12h20M12 2c3 3 3 17 0 20M12 2c-3 3-3 17 0 20" fill="none" stroke="#f4f4f4" stroke-width="1.4"/></svg>
        <span>www.northlandsbluewagon.net</span>
      </li>
    </ul>

    <address class="address" style="font-style:normal">
      4470 Cedar Hollow Road<br>Pine Falls Maine 10384
    </address>
  </section>

  <section class="card card-back">
    <div class="back-mark"><span class="dot"></span><span>Northland's Blue Wagon</span></div>
    <p class="back-url">www.northlandsbluewagon.net</p>
  </section>
</main>
</body>
</html>
```